Landscape Company in need of logo and business card update. Current logo file is attached.

I need a business card design for a Woman Owned Landscape business in Kansas City. I do Native plant installation and maintenance as well as mowing, chemical applications and residential and commercial landscaping.
My colors are navy, green and white.
I currently have a logo that can be used or you can redesign it.

Target Market(s)

Residential and commercial

Industry/Entity Type

Landscape

Contact Information for Business Card

On back of current card it lists what I do and website:
BMP/Raingarden Maintenance and Installation, Certified Chemical Applicator for Trees, shrubs, and turf; Landscape Design and Installation for residential and commercial.

Logo Text

Copperleaf Landscape Services, LLC

Font styles to use
Other font styles liked:
• See current font on logo examples

Requirements
Must have
• Phone number: 816-402-7719
• Website: www.copperleaflandscape-example.com
• Colors: Navy, Green, white
• Email: copperleaflandscape@mailbox-example.com
• Address: PO BOX 471208 Shawnee, KS 66219
• Name of Person: Marcy Dulwick, owner

```html
<!DOCTYPE html>
<html lang="en">
<head>
<meta charset="utf-8">
<title>Copperleaf Landscape Services — Business Card</title>
<link rel="stylesheet" href="https://fonts.googleapis.com/css2?family=Inter:wght@300;400;600&display=swap">
<style>
  :root {
    --bg: #ececec;
    --card: #f9f9f9;
    --navy: #4b5877;
    --navy-deep: #2f3c5c;
    --green: #25c383;
  }
  * { margin: 0; padding: 0; box-sizing: border-box; }
  html, body { width: 1200px; height: 800px; overflow: hidden; }
  body {
    background: var(--bg);
    font-family: "Inter", Arial, sans-serif;
    display: flex;
    align-items: center;
    justify-content: center;
  }
  .business-card {
    position: relative;
    width: 400px;
    height: 700px;
    background: var(--card);
  }
  .brand {
    position: absolute;
    left: 26px;
    top: 38px;
    display: flex;
    align-items: flex-start;
    gap: 14px;
  }
  .brand-mark {
    width: 20px;
    height: 20px;
    background: var(--green);
    margin-top: 2px;
  }
  .brand-name {
    font-size: 13px;
    font-weight: 400;
    line-height: 1.3;
    color: var(--navy-deep);
    width: 150px;
  }
  .owner {
    position: absolute;
    left: 26px;
    top: 385px;
    color: var(--green);
  }
  .owner-name {
    font-size: 32px;
    line-height: 1.1;
    letter-spacing: -0.5px;
  }
  .owner-name .first { font-weight: 300; }
  .owner-name .last { font-weight: 600; }
  .owner-title {
    font-size: 13px;
    font-weight: 300;
    margin-top: 2px;
  }
  .contact {
    position: absolute;
    left: 26px;
    top: 575px;
    list-style: none;
    color: var(--navy);
    font-size: 13px;
    font-weight: 300;
    line-height: 27px;
  }
</style>
</head>
<body>
  <article class="business-card">
    <header class="brand">
      <span class="brand-mark"></span>
      <span class="brand-name">Copperleaf Landscape Services, LLC</span>
    </header>

    <section class="owner">
      <h1 class="owner-name"><span class="first">Marcy</span> <span class="last">Dulwick</span></h1>
      <p class="owner-title">Owner</p>
    </section>

    <ul class="contact">
      <li class="contact-address">PO BOX 471208 Shawnee, KS 66219</li>
      <li class="contact-phone">816-402-7719</li>
      <li class="contact-email">copperleaflandscape@mailbox-example.com</li>
      <li class="contact-web">www.copperleaflandscape-example.com</li>
    </ul>
  </article>
</body>
</html>
```